Lone Prairie Canvas & Sound Jubilee

Organization:
Lone Prairie Canvas and Sound Jubilee is a non-profit organization created by a group of anonymous donors to bring more fun, culture, and art to a small Texas town. Our mission is to promote art and music in Washington County.
The multi-day eclectic festival will feature three stages, a film, art vendors, live mural artists, and food trucks set up throughout historic downtown Brenham. The event is FREE to the public.
Goals:
We need an attractive poster to publicize the festival.
Details:
Lone Prairie Canvas and Sound Jubilee
Friday, October 14 – 16
Free admission (VIP tickets available)
Live music- 3 stages/10 bands
Film Screening
Art vendors and art walk
Live art murals
Food trucks
www.loneprairiecanvasandsoundjubilee.example
#loneprairiecanvasandsound
Requirements:
Please incorporate our festival logo attached.
Conclusion:
After selecting a poster design, we hope to continue to work with the artist to design other event materials including website splash page and rack cards using design elements from the poster.

```html
<!DOCTYPE html>
<html lang="en">
<head>
<meta charset="utf-8">
<title>Lone Prairie Canvas and Sound Jubilee — Poster</title>
<link rel="stylesheet" href="https://fonts.googleapis.com/css2?family=Alfa+Slab+One&family=Didact+Gothic&family=Arimo:wght@700&family=Roboto+Condensed:wght@500&display=swap">
<style>
  :root {
    --page: #ffffff;
    --ink: #000000;
    --ember-light: #fff4b0;
    --ember-gold: #f9c13a;
    --ember-orange: #ea7a16;
    --ember-deep: #b53a0a;
    --ember-dark: #5a1404;
    --crowd: #0a0502;
    --copy: #f4f4f4;
    --rule: #3c4650;
    --alert: #ee1410;
    --slash: #5a5a5a;
  }
  * { margin: 0; padding: 0; box-sizing: border-box; }
  html, body {
    width: 1200px; height: 1200px; overflow: hidden;
    background: var(--page);
  }
  .poster {
    position: absolute;
    left: 209px; top: 47px;
    width: 782px; height: 1106px;
    background: var(--ink);
    overflow: hidden;
  }
  .stage-art {
    position: absolute; left: 0; top: 0;
    width: 782px; height: 780px;
    background:
      linear-gradient(to bottom,
        rgba(10,5,2,0) 0%, rgba(10,5,2,0) 58%,
        rgba(10,5,2,0.55) 66%, rgba(10,5,2,0.88) 76%,
        var(--ink) 96%),
      radial-gradient(ellipse 560px 520px at 400px 430px,
        var(--ember-light) 0%, var(--ember-gold) 32%,
        var(--ember-orange) 60%, var(--ember-deep) 84%, var(--ember-dark) 100%);
  }
  .headline {
    position: absolute; left: 0; top: 0;
    width: 782px; height: 560px;
  }
  .headline text { fill: var(--ink); }
  .date-day, .date-month { font-family: "Alfa Slab One", serif; }
  .festival-name { font-family: "Alfa Slab One", serif; fill: #1a1004 !important; }

  .brand {
    position: absolute; left: 622px; top: 39px;
    width: 150px;
    display: flex; flex-direction: column; align-items: center; gap: 9px;
  }
  .brand-mark { width: 70px; height: 70px; background: #ffffff; }
  .brand-name {
    font-family: "Roboto Condensed", sans-serif; font-weight: 500;
    font-size: 8.4px; color: #ffffff; white-space: nowrap;
  }

  .highlights {
    position: absolute; left: 0; top: 780px; width: 782px;
    list-style: none; text-align: center;
    font-family: "Didact Gothic", sans-serif; font-size: 28px; color: var(--copy);
  }
  .highlights li { height: 50px; line-height: 44px; position: relative; }
  .highlights li + li::before {
    content: ""; position: absolute; left: 50%; top: -3px;
    width: 170px; height: 1px; margin-left: -85px;
    background: linear-gradient(to right, transparent, var(--rule), transparent);
  }
  .admission {
    position: absolute; left: 0; top: 1038px; width: 782px;
    text-align: center;
    font-family: "Arimo", sans-serif; font-weight: 700; font-size: 29px;
    color: var(--alert);
  }
  .admission .divider { color: var(--slash); }
</style>
</head>
<body>
  <main class="poster">
    <div class="stage-art" role="img" aria-label="Fiery concert lights with a guitar and a cheering crowd in silhouette, arms raised"></div>

    <svg class="headline" viewBox="0 0 782 560" width="782" height="560">
      <defs>
        <filter id="glow" x="-20%" y="-20%" width="140%" height="140%">
          <feDropShadow dx="0" dy="0" stdDeviation="6" flood-color="#fff4c0" flood-opacity="0.8"/>
        </filter>
      </defs>
      <text class="date-day" x="391" y="353" text-anchor="middle" font-size="405" textLength="406" lengthAdjust="spacingAndGlyphs" filter="url(#glow)">14</text>
      <text class="date-month" x="391" y="415" text-anchor="middle" font-size="60" textLength="420" lengthAdjust="spacingAndGlyphs" filter="url(#glow)">OCTOBER 2016</text>
      <text class="festival-name" x="391" y="461" text-anchor="middle" font-size="33" textLength="532" lengthAdjust="spacingAndGlyphs">LONE PRAIRIE CANVAS AND SOUND JUBILEE</text>
    </svg>

    <div class="brand">
      <span class="brand-mark"></span>
      <span class="brand-name">LONE PRAIRIE CANVAS AND SOUND JUBILEE</span>
    </div>

    <ul class="highlights">
      <li>Live music -3 stages / 10 bands</li>
      <li>Film screening</li>
      <li>Art vendors and art walk</li>
      <li>Live art murals</li>
      <li>Food trucks</li>
    </ul>

    <p class="admission">FREE Admission <span class="divider">/</span> VIP Tickets Available</p>
  </main>
</body>
</html>
```